Silver Arch Consulting Website Design

I already have a live website. Just want some help with design, finishing up the project. I also have another site with wix that I am ready to have designed. I am not completely sure on the pages but will for sure need "coaching", "training", "resources". Most of the people I currently work with are real estate brokers and mortgage brokers but I want to be able to appeal to all industries.
Number of Pages Required
4 page
Font styles to use
Sans Serif
Colors
Requirements
Must have
- place holders for video
Nice to have
- a way for people to purchase digital downloads

```html
<!DOCTYPE html>
<html lang="en">
<head>
<meta charset="utf-8">
<title>Silver Arch Consulting</title>
<link href="https://fonts.googleapis.com/css2?family=Montserrat:wght@400;500;600;700&family=Mulish:wght@300;400;600&display=swap" rel="stylesheet">
<style>
:root{
  --red:#e8292c;
  --maroon:#4c1217;
  --maroon-deep:#2c0a0d;
  --ink:#3a3a3a;
  --muted:#6b6b6b;
  --line:#cfcfcf;
  --white:#ffffff;
}
*{box-sizing:border-box;margin:0;padding:0}
html,body{width:1200px;height:2853px;overflow:hidden}
body{position:relative;background:var(--white);font-family:"Mulish",sans-serif;color:var(--ink)}
.abs{position:absolute}

/* hero */
.hero{left:0;top:0;width:1200px;height:515px;background:linear-gradient(135deg,#6a1f24 0%,#4c1217 45%,#3a0c10 100%)}
.brand{left:100px;top:34px;display:flex;align-items:center;gap:12px}
.brand-mark{width:38px;height:38px;background:var(--red)}
.brand-name{font-family:"Montserrat",sans-serif;font-weight:700;font-size:17px;color:var(--white);line-height:1.15}
.brand-tag{font-family:"Montserrat",sans-serif;font-weight:700;font-size:17px;color:var(--white)}
.btn{display:flex;align-items:center;justify-content:center;font-family:"Montserrat",sans-serif;font-weight:600;font-size:13px;color:var(--white);border-radius:4px}
.btn-book{left:831px;top:32px;width:129px;height:42px;background:var(--red)}
.btn-login{left:970px;top:32px;width:129px;height:42px;border:1.5px solid var(--white)}
.hero-title{left:200px;top:218px;font-family:"Montserrat",sans-serif;font-weight:600;font-size:22px;color:var(--white)}
.hero-text{left:200px;top:260px;width:490px;font-size:13.5px;line-height:21px;color:var(--white)}
.btn-more{left:200px;top:358px;width:129px;height:43px;border:1.5px solid var(--white);font-weight:500}

/* story */
.section-title{left:0;width:1200px;text-align:center;font-family:"Montserrat",sans-serif;font-weight:500;font-size:27px;color:var(--red)}
.story-title{top:578px}
.story-text{left:198px;top:650px;width:804px;text-align:center;font-size:13px;line-height:22px;color:var(--muted)}
.video{left:457px;top:763px;width:285px;height:161px;border-radius:8px;background:linear-gradient(160deg,#5c5a3a,#2e2a1c)}
.play{left:584px;top:829px}

/* services */
.card-photo{top:1090px;width:301px;height:222px}
.card-title{top:1348px;width:301px;text-align:center;font-family:"Montserrat",sans-serif;font-weight:600;font-size:12px;line-height:21px;color:var(--red)}
.card-text{top:1403px;width:301px;padding:0 12px;text-align:center;font-size:11.5px;line-height:21px;color:var(--ink)}

/* testimonial */
.quote-band{left:0;top:1643px;width:1200px;height:335px;background:linear-gradient(180deg,#5a1a1f,#46101a 60%,#3b0d12)}
.quote-icon{left:565px;top:1705px}
.quote-text{left:240px;top:1783px;width:720px;text-align:center;font-size:15px;line-height:22px;color:var(--white)}
.quote-name{left:0;top:1868px;width:1200px;text-align:center;font-size:15px;color:var(--white)}
.arrow-left{left:98px;top:1784px}
.arrow-right{left:1080px;top:1784px}

/* contact */
.contact-title{top:2125px}
.field{border-bottom:1px solid var(--line);font-size:11px;color:var(--muted);padding:0 0 10px 12px}
.f-name{left:398px;top:2243px;width:190px;height:27px}
.f-email{left:612px;top:2243px;width:187px;height:27px}
.f-subject{left:398px;top:2306px;width:401px;height:27px}
.f-message{left:398px;top:2355px;width:401px;height:114px}
.btn-send{left:519px;top:2528px;width:156px;height:42px;background:var(--red);border-radius:0;font-size:15px}

/* footer */
.footer{left:0;top:2700px}
.copyright{left:100px;top:2777px;font-size:11px;color:#b9a9aa}
.social{top:2771px;width:18px;height:18px;background:#3d5a9a}
.social-b{background:#1b76b5}
.subscribe-label{left:814px;top:2742px;font-size:12px;color:var(--white)}
.sub-input{left:801px;top:2769px;width:217px;height:35px;border:1px solid #bfaeb0;font-size:10px;color:#d9cfd0;padding:12px 14px}
.btn-sub{left:1035px;top:2769px;width:64px;height:35px;background:var(--red);border-radius:0;font-size:10px}
</style>
</head>
<body>

<section class="abs hero" role="img" aria-label="Overhead photo of a business team working around a table with papers, tinted dark red"></section>
<div class="abs brand">
  <span class="brand-mark"></span>
  <div>
    <div class="brand-name">SILVER ARCH CONSULTING LLC</div>
    <div class="brand-name" style="font-size:12px;font-weight:500">Love What You Do</div>
  </div>
</div>
<a class="abs btn btn-book">Book Online</a>
<a class="abs btn btn-login">Client Log In</a>
<h1 class="abs hero-title">IT'S GROW TIME</h1>
<p class="abs hero-text">From making strategic decisions to developing your capabilities, I'm here to help. Using my expertise and deep understanding of the industry, you'll receive real solutions and experience true results. Get in touch to book a meeting.</p>
<a class="abs btn btn-more">Learn More</a>

<h2 class="abs section-title story-title">MY STORY</h2>
<p class="abs story-text">I've been a professional Business Coach since 2010. I believe in maintaining a positive mindset, creating partnerships with a purpose, and always striving for significant outcomes. When you work with me, you should expect a collaboration with transparency and consistency. Want to learn more? Contact me today for an initial consultation.</p>
<div class="abs video" role="img" aria-label="Video placeholder showing a speaker presenting to a seated audience"></div>
<svg class="abs play" width="30" height="30" viewBox="0 0 30 30"><path d="M10 7 L23 15 L10 23 Z" fill="#ffffff"/></svg>

<div class="abs card-photo" style="left:99px;background:linear-gradient(180deg,#d8d6d2,#6e5e52)" role="img" aria-label="Audience seated at a conference seen from behind"></div>
<div class="abs card-photo" style="left:449px;background:linear-gradient(180deg,#eef2f4 0%,#9aa6ad 55%,#3f7c86 100%)" role="img" aria-label="Silhouettes of business people standing by a window over a meeting table"></div>
<div class="abs card-photo" style="left:799px;background:linear-gradient(160deg,#e6eef4,#5a6b80)" role="img" aria-label="Two colleagues in suits discussing work at a laptop"></div>

<h3 class="abs card-title" style="left:99px">BUSINESS PERFORMANCE<br>CONSULTING</h3>
<h3 class="abs card-title" style="left:449px">BUSINESS PERFORMANCE<br>CONSULTING</h3>
<h3 class="abs card-title" style="left:799px">BUSINESS PERFORMANCE<br>CONSULTING</h3>
<p class="abs card-text" style="left:99px">By analyzing your systems, tools and people, I will identify strategies to get your business running at optimal efficiency. Book an introductory meeting today to learn more about how I can make your business thrive.</p>
<p class="abs card-text" style="left:449px">By analyzing your systems, tools and people, I will identify strategies to get your business running at optimal efficiency. Book an introductory meeting today to learn more about how I can make your business thrive.</p>
<p class="abs card-text" style="left:799px">By analyzing your systems, tools and people, I will identify strategies to get your business running at optimal efficiency. Book an introductory meeting today to learn more about how I can make your business thrive.</p>

<section class="abs quote-band" role="img" aria-label="Blurred crowd at a seminar, tinted dark red"></section>
<svg class="abs quote-icon" width="70" height="44" viewBox="0 0 70 44" fill="none" stroke="#ffffff" stroke-width="2.5">
  <path d="M8 6 h26 a6 6 0 0 1 6 6 v8 a6 6 0 0 1 -6 6 h-14 l-8 7 v-7 h-4 a6 6 0 0 1 -6 -6 v-8 a6 6 0 0 1 6 -6z"/>
  <path d="M30 14 h28 a6 6 0 0 1 6 6 v8 a6 6 0 0 1 -6 6 h-2 v7 l-8 -7 h-18 a6 6 0 0 1 -6 -6 v-8 a6 6 0 0 1 6 -6z" fill="#4c1217"/>
  <path d="M38 22 h18 M38 27 h12"/>
</svg>
<svg class="abs arrow-left" width="22" height="42" viewBox="0 0 22 42"><path d="M20 2 L2 21 L20 40" fill="none" stroke="#ffffff" stroke-width="1.5"/></svg>
<svg class="abs arrow-right" width="22" height="42" viewBox="0 0 22 42"><path d="M2 2 L20 21 L2 40" fill="none" stroke="#ffffff" stroke-width="1.5"/></svg>
<p class="abs quote-text">Daniel was my first mentor and trainer in real estate. He pushed me from nobody to rookie of the year International. He is that person who will bring the best out of you! I am forever grateful for his coaching and mentorship!</p>
<p class="abs quote-name">Owen Hartley</p>

<h2 class="abs section-title contact-title">CONTACT ME</h2>
<div class="abs field f-name">Name</div>
<div class="abs field f-email">Email</div>
<div class="abs field f-subject">Subject</div>
<div class="abs field f-message">Message</div>
<a class="abs btn btn-send">SEND</a>

<svg class="abs footer" width="1200" height="153" viewBox="0 0 1200 153" preserveAspectRatio="none">
  <path d="M0 38 Q600 -30 1200 38 L1200 153 L0 153 Z" fill="#2c0a0d"/>
</svg>
<p class="abs copyright">©2018 by Silver Arch Consulting LLC.</p>
<span class="abs social" style="left:552px"></span>
<span class="abs social social-b" style="left:588px"></span>
<p class="abs subscribe-label">Subscribe</p>
<div class="abs sub-input">Email Address</div>
<a class="abs btn btn-sub">SEND</a>

</body>
</html>
```